Redesign Home Page

We need a new home page with a white background. Our company provides singing instruction to students world wide, both in person and on line. We're looking for a very clean and open design with maximum white space. The main goal of the page will be to get users to sign up for our mailing list. The current site is www.kelvarsong.com. I think the new page can be a long page (scrolll down is ok), to allow for more white space while still using the text from the current page.
Updates

Project Deadline Extended
Reason: Hello to all Designers, I apologize for not giving feedback this weekend. We went out of town for the Memorial Day holiday and I had no internet. I will be extending the deadline to Thursday. -Marcus

Target Market(s)

Singers of all ages and abilities, especially beginners.

Industry/Entity Type

It Company

Requirements
Must have
• 1. A white background
2. Lots of open space
3. An email sign up form on the top right that reads:
a. “Improve Your Singing Now.
b. Sign up for our Free Video Series: Tone Quest
4. Testimonails: found on https://www.kelvarsong.com/tone-ascent
5. My logo with the piano
6. My photo
7. Learn about our Lessons in:
a. San Francisco
b. Alameda
8. On Line Programs:
a. Tone Ascent
b. Wavlo Lessons

Nice to have
• Link to current student page: http://kelvarsong.com/what-students-say/students2
Pictures of singers
Video box: Use Marcus_Example
Should not have
• See "KelvarSong Redesign" file for more details.

```html
<!DOCTYPE html>
<html lang="en">
<head>
<meta charset="utf-8">
<title>Marcus Hale School of Voice</title>
<link href="https://fonts.googleapis.com/css2?family=Ubuntu:ital,wght@0,300;0,400;1,300&display=swap" rel="stylesheet">
<style>
:root{
  --blue:#29a3dc;
  --ink:#1c1c1c;
  --text:#3a3a3a;
  --muted:#555;
  --line:#c8c8c8;
  --footer:#f4f4f4;
  --white:#fff;
}
*{margin:0;padding:0;box-sizing:border-box}
html,body{width:1186px;height:1200px;overflow:hidden;background:var(--white)}
body{position:relative;font-family:"Ubuntu",sans-serif;font-weight:300;color:var(--text)}
.abs{position:absolute}
.brand{display:flex;align-items:center;gap:10px}
.brand-mark{width:26px;height:26px;background:var(--blue)}
.brand-name{font-size:24px;font-weight:400;color:#444;white-space:nowrap}
.brand-sub{font-size:12px;font-weight:400;color:#444}
.nav a{position:absolute;top:0;height:49px;display:flex;align-items:flex-end;padding-bottom:8px;font-size:14px;color:var(--ink);text-decoration:none;line-height:13px;text-align:center;justify-content:center}
.nav .active{background:var(--blue);color:var(--white);width:66px;left:390px}
.caret{color:var(--blue);font-size:10px;margin-left:3px}
.social{width:24px;height:24px;background:var(--blue)}
.nl-title{font-size:17px;font-weight:400;color:var(--ink);white-space:nowrap;line-height:20px}
.nl-input{height:31px;border:1px solid #bbb;background:var(--white);font-size:9px;font-style:italic;color:#888;padding:11px 0 0 34px;white-space:nowrap}
.nl-ok{height:31px;width:34px;background:var(--blue);color:var(--white);font-size:14px;display:flex;align-items:center;justify-content:center}
.nl-list{list-style:none;font-size:13.5px;color:var(--ink);line-height:17px;white-space:nowrap}
.nl-list li::before{content:"";display:inline-block;width:6px;height:6px;border-radius:50%;background:var(--blue);margin:0 8px 2px 0}
.cover{width:92px;height:80px;background:linear-gradient(135deg,#1a1f4a 0%,#5a2d7a 55%,#9aa 100%);border-radius:3px}
.hero-title{left:0;width:1231px;text-align:center;top:187px;font-size:25px;font-weight:400;color:var(--ink)}
.hero-sub{left:0;width:1231px;text-align:center;top:219px;font-size:13px;line-height:18px;color:var(--ink)}
.hero-photo{left:437px;top:268px;width:354px;height:215px;background:radial-gradient(ellipse at 40% 10%,#d9ecff 0,#3d8fe0 25%,#0b3a8a 60%,#020c2a 100%)}
.btn{left:566px;top:492px;width:93px;height:29px;background:var(--blue);color:var(--white);font-size:14px;display:flex;align-items:center;justify-content:center;box-shadow:0 2px 0 #1c7fb0}
.rule{left:0;width:1186px;border-top:1px dashed var(--line)}
.adv-title{left:0;width:1231px;text-align:center;top:551px;font-size:20px;font-weight:400;color:var(--ink)}
.adv-copy{left:389px;top:580px;width:447px;font-size:10.5px;line-height:14.5px;text-align:justify;text-align-last:center;color:var(--ink)}
.feature{width:150px;top:682px}
.feature svg{display:block;margin:0 auto;height:36px}
.feature h3{margin-top:24px;font-size:13.5px;font-weight:400;color:var(--ink);text-align:center;white-space:nowrap}
.feature p{margin:10px auto 0;width:140px;font-size:9.3px;line-height:13.4px;text-align:justify;color:var(--muted)}
.footer{left:0;top:926px;width:1186px;height:252px;background:var(--footer)}
.f-head{font-size:12px;font-weight:400;color:var(--ink);border-bottom:1px solid var(--blue);padding-bottom:1px}
.f-link{font-size:9.5px;font-style:italic;color:#444}
.copyright{left:0;width:1231px;text-align:center;top:1162px;font-size:8px;color:#444;font-weight:400}
</style>
</head>
<body>
<header>
  <div class="abs brand" style="left:126px;top:14px">
    <span class="brand-mark"></span>
    <div><div class="brand-name">Marcus Hale</div><div class="brand-sub">School of Voice</div></div>
  </div>
  <nav class="nav">
    <a class="active" href="#">home</a>
    <a href="#" style="left:474px;width:70px">voice<br>lessons<span class="caret">v</span></a>
    <a href="#" style="left:570px;width:38px">blog</a>
    <a href="#" style="left:636px;width:96px">students<br>testimonials<span class="caret">v</span></a>
    <a href="#" style="left:755px;width:84px">meet the<br>instructors<span class="caret">v</span></a>
    <a href="#" style="left:862px;width:126px">tone ascent</a>
  </nav>
  <span class="abs social" style="left:1007px;top:21px"></span>
  <span class="abs social" style="left:1033px;top:21px"></span>
</header>

<section>
  <div class="abs cover" role="img" aria-label="Tone Ascent DVD box set" style="left:598px;top:68px"></div>
  <div class="abs nl-title" style="left:704px;top:79px">Newsletter</div>
  <div class="abs nl-input" style="left:797px;top:74px;width:230px">enter your email here...</div>
  <div class="abs nl-ok" style="left:1027px;top:74px">OK</div>
  <ul class="abs nl-list" style="left:705px;top:114px">
    <li>Improve Your Singing Now</li>
    <li>Sign up for our Free Video Series: Tone Quest</li>
  </ul>
</section>

<section>
  <h1 class="abs hero-title">PROFESSIONAL VOCAL COACH</h1>
  <p class="abs hero-sub">MARCUS D. HALE HAS LAID THE VOCAL FOUNDATION FOR<br>THOUSANDS OF SINGERS WORLDWIDE, FOR 20+ YEARS</p>
  <div class="abs hero-photo" role="img" aria-label="Concert crowd with raised hands under blue stage lights"></div>
  <a class="abs btn">more info</a>
</section>

<div class="abs rule" style="top:538px"></div>

<section>
  <h2 class="abs adv-title">ADVANTAGES of working with Tone Ascent</h2>
  <p class="abs adv-copy">After many years of work, I've decided that the effective transformation of the human voice is my life's work and passion. While on line methods of instruction are not a as effective as in person lessons, I find that getting a foundational understanding of the voice that comes with Tone Ascent can greatly enhance your singing voice, whether you're currently studying with a teacher or working on your own.</p>

  <div class="abs feature" style="left:166px">
    <svg viewBox="0 0 36 36"><circle cx="18" cy="18" r="15" fill="none" stroke="var(--blue)" stroke-width="4"/><path d="M18 9v10h7" fill="none" stroke="var(--blue)" stroke-width="3"/></svg>
    <h3>Flexibility is paramount</h3>
    <p>Your schedule may not permit attending weekly singing classes as a set time and location. With Tone Ascent, you can practice in the kitchen, in your car, in the shower....</p>
  </div>
  <div class="abs feature" style="left:354px">
    <svg viewBox="0 0 36 36"><rect x="6" y="1" width="24" height="34" fill="none" stroke="var(--blue)" stroke-width="2.5"/><path d="M6 8h24M6 14h24M6 20h24M6 26h24" stroke="var(--blue)" stroke-width="2.5"/></svg>
    <h3>Downloadable content</h3>
    <p>All of the lessons of Tone Ascent are offered both in a streaming format and as downloads. That way you can check in with your own personal singing teacher from any of your devices.</p>
  </div>
  <div class="abs feature" style="left:540px">
    <svg viewBox="0 0 36 36"><rect x="1" y="22" width="10" height="12" fill="var(--blue)"/><rect x="13" y="4" width="10" height="30" fill="var(--blue)"/><rect x="25" y="14" width="10" height="20" fill="var(--blue)"/></svg>
    <h3>Adaptable course format</h3>
    <p>Tone Ascent is structured into a series of lessons that build on one another. However, since each of the Five Systems are intimately interdependent, you can always return to earlier lessons to deepen your overall understanding.</p>
  </div>
  <div class="abs feature" style="left:726px">
    <svg viewBox="0 0 48 36"><circle cx="9" cy="9" r="5" fill="var(--blue)"/><circle cx="38" cy="9" r="5" fill="var(--blue)"/><path d="M1 34c0-10 4-15 8-15s8 5 8 15zM30 34c0-10 4-15 8-15s8 5 8 15z" fill="var(--blue)"/><circle cx="21" cy="16" r="2" fill="var(--blue)"/><circle cx="26" cy="16" r="2" fill="var(--blue)"/><circle cx="23.5" cy="22" r="2" fill="var(--blue)"/></svg>
    <h3>Personal interaction</h3>
    <p>I'm committed to your success. I'm here to help you apply these principles to your singing. I offer a free Wavlo consultation to everyone who purchases Tone Ascent.</p>
  </div>
  <div class="abs feature" style="left:910px">
    <svg viewBox="0 0 36 36"><circle cx="26" cy="9" r="7" fill="var(--blue)"/><path d="M21 14L6 30l3 3 16-14" fill="none" stroke="var(--blue)" stroke-width="3"/><path d="M7 31c-4 3-4 5 1 5" fill="none" stroke="var(--blue)" stroke-width="2"/></svg>
    <h3>Vocal health education</h3>
    <p>One of the jobs I take most seriously is the importance of teaching vocal health to singers from the very beginning. Making Tone Ascent the next stage of your own vocal development will help you form</p>
  </div>
</section>

<div class="abs rule" style="top:912px"></div>

<footer class="abs footer"></footer>
<div class="abs brand" style="left:514px;top:944px">
  <span class="brand-mark"></span>
  <div><div class="brand-name">Marcus Hale</div><div class="brand-sub">School of Voice</div></div>
</div>
<div class="abs f-head" style="left:236px;top:1023px">Information</div>
<div class="abs f-link" style="left:237px;top:1048px">Home</div>
<div class="abs f-link" style="left:237px;top:1070px">Voice Sessions</div>
<div class="abs f-link" style="left:237px;top:1091px">Blog</div>
<div class="abs f-link" style="left:334px;top:1046px">Students testimonials</div>
<div class="abs f-link" style="left:334px;top:1068px">Meet the Instructors</div>
<div class="abs f-link" style="left:334px;top:1090px">Tone Ascent</div>
<div class="abs f-head" style="left:509px;top:1025px">Where to find us ?</div>
<div class="abs f-link" style="left:517px;top:1050px">Alemada</div>
<div class="abs f-link" style="left:517px;top:1070px">San Franciso</div>
<div class="abs f-link" style="left:517px;top:1091px">Online</div>

<div class="abs nl-title" style="left:680px;top:1017px">Newsletter</div>
<div class="abs nl-input" style="left:773px;top:1012px;width:230px">enter your email here...</div>
<div class="abs nl-ok" style="left:1003px;top:1012px">OK</div>
<ul class="abs nl-list" style="left:681px;top:1052px">
  <li>Improve Your Singing Now</li>
  <li>Sign up for our Free Video Series: Tone Quest</li>
</ul>
<div class="abs" style="left:838px;top:1114px;font-size:10px;color:var(--ink);font-weight:400">Find Us on:</div>
<span class="abs social" style="left:896px;top:1108px"></span>
<span class="abs social" style="left:923px;top:1108px"></span>

<div class="abs copyright">Copyrights (c) 2014- Marcus D. Hale School of Voice- All rights Reserved &nbsp;| &nbsp;Privacy Policy &nbsp;| &nbsp;Terms of Use &nbsp;| &nbsp;Sitemap</div>
</body>
</html>
```